Brisvale services brochure

We need a new company brochure. The brochure will be formatted for PDF distribution but should be printable on "letter" size paper. 2 pages plus front and back cover. Color white and same blue as logo. Logo "O" should be used as design. Look at webpage for general info: www.brisvale.ca<br/><br/>Front cover: pic1, logo, design and "Your Cleaning is Our Business". <br/>Back cover" "O" design, logo and info from "contact" page<br/>Front cover inside: design and intro from web home page, also use stock pics of clean offices ect as placeholders for purchased pics.<br/>1st page: design and "Our Services", use info of "Cleanroom & GMP Services", "Janitorial Services" from services page.<br/>2nd page: design and "Special Services", info from "Carpet & Upholstery Services", "Window Cleaning Services", and list of "Other Services".<br/>Back cover inside : design and info from technology page, use stock pics for place holders.

Industry/Entity Type

Janitorial

Font styles to use
Sans Serif
Other font styles liked:
• Futura Book

Colors
0555a3

Requirements
Must have
• The logo "O" (target) should be part of the design. Design color same as logo.

```html
<!DOCTYPE html>
<html lang="en">
<head>
<meta charset="utf-8">
<title>Brisvale Services Brochure</title>
<link href="https://fonts.googleapis.com/css2?family=Montserrat:wght@400;500;600;700;800&display=swap" rel="stylesheet">
<style>
:root{
  --brand:#0555a3;
  --navy:#0a4680;
  --deep:#083a6b;
  --sky:#1a7fd0;
  --light:#2aa8e2;
  --ink:#1c3557;
  --grey:#6d6d6d;
  --text:#4a4a4a;
  --paper:#ffffff;
  --stage:#e4e5e9;
}
*{margin:0;padding:0;box-sizing:border-box}
html,body{width:1200px;height:2257px;overflow:hidden;background:var(--stage)}
body{position:relative;font-family:"Montserrat",sans-serif;color:var(--text)}
.page{position:absolute;width:520px;height:673px;background:var(--paper);overflow:hidden;box-shadow:0 8px 24px rgba(0,0,0,.12)}
.page svg.art{position:absolute;inset:0}
.spread-fold{position:absolute;width:1px;height:673px;background:rgba(0,0,0,.08)}

/* brand name */
.brand-name{position:absolute;display:flex;align-items:center;gap:10px;font-family:"Montserrat",sans-serif;font-weight:500;color:var(--sky);letter-spacing:.28em;font-size:34px}
.brand-name .dot{width:14px;height:14px;border-radius:50%;background:var(--sky)}

/* front cover */
.cover-headline{position:absolute;left:0;right:0;text-align:center;font-weight:800;line-height:1}
.cover-headline .l1{display:block;color:var(--sky);font-size:46px;letter-spacing:.01em}
.cover-headline .l2{display:block;color:var(--ink);font-size:33px;margin-top:6px}
.cover-rule{position:absolute;left:185px;width:150px;height:2px;background:var(--sky)}
.cover-url{position:absolute;left:0;right:0;text-align:center;color:var(--brand);font-weight:600;font-size:15px;letter-spacing:.22em}

/* inside left */
.intro-title{position:absolute;left:34px;top:34px;width:440px;font-weight:800;color:var(--sky);font-size:26px;line-height:1.05}
.intro-title span{color:var(--ink)}
.intro-copy{position:absolute;left:34px;top:104px;width:440px;font-size:10.5px;line-height:1.45;color:var(--text)}
.section-title{position:absolute;left:34px;top:182px;font-weight:800;color:var(--sky);font-size:21px}
.services-panel{position:absolute;left:40px;top:222px;width:446px;height:418px;border-radius:18px;background:radial-gradient(circle at 75% 60%,#0f5aa0,var(--deep) 75%)}
.service{position:absolute;left:0;width:100%;height:62px}
.service .badge{position:absolute;left:-20px;top:6px;width:44px;height:44px;border-radius:50%;background:var(--paper);border:4px solid var(--sky)}
.service .badge i{position:absolute;inset:7px;border-radius:50%;background:var(--light)}
.service h3{position:absolute;left:40px;top:6px;font-size:14px;font-weight:700;color:#fff;letter-spacing:.02em;line-height:1.1}
.service p{position:absolute;left:40px;top:25px;width:380px;font-size:9.5px;line-height:1.35;color:#d4e4f5}

/* inside right */
.qc-band{position:absolute;left:232px;top:58px;width:288px;height:170px;background:var(--grey);padding:18px 18px 0 58px;color:#fff}
.qc-band h2{font-size:17px;font-weight:800;line-height:1.1}
.qc-band h2 span{font-weight:500}
.qc-band p{font-size:9.5px;line-height:1.4;margin-top:8px;color:#f1f1f1}
.feature{position:absolute;width:210px}
.feature h4{display:flex;align-items:center;gap:7px;font-size:14px;font-weight:700;color:var(--brand);line-height:1.1}
.feature h4 svg{flex:none}
.feature p{margin:5px 0 0 25px;font-size:9.5px;line-height:1.4;color:var(--text)}
.timekeeping{position:absolute;left:34px;top:466px;width:452px}
.timekeeping h3{font-size:17px;font-weight:800;color:var(--brand)}
.timekeeping p{font-size:9.5px;line-height:1.4;margin-top:4px}
.timekeeping ul{list-style:none;margin-top:5px}
.timekeeping li{position:relative;padding-left:14px;font-size:9px;line-height:1.45}
.timekeeping li::before{content:"";position:absolute;left:0;top:3px;width:7px;height:7px;border-radius:50%;border:1.5px solid var(--sky)}

/* back cover */
.contact-block{position:absolute;left:0;right:0;top:178px;text-align:center;color:#fff}
.contact-block h2{font-size:17px;font-weight:800;letter-spacing:.02em;margin-bottom:12px}
.contact-line{display:flex;flex-direction:column;align-items:center;gap:3px;font-size:14px;font-weight:500;margin-bottom:8px}
.contact-hours{font-size:14px;font-weight:500;margin-top:4px}
.social{position:absolute;left:398px;top:556px;display:flex;gap:10px}
.social span{width:16px;height:16px;border-radius:50%;background:var(--ink)}
</style>
</head>
<body>

<!-- ROW 1: front cover -->
<section class="page front-cover" style="left:340px;top:60px">
  <svg class="art" width="520" height="673" viewBox="0 0 520 673">
    <polygon points="0,230 180,230 150,470 0,470" fill="var(--navy)"/>
    <polygon points="345,120 520,95 520,205 405,238" fill="var(--navy)"/>
    <polygon points="420,255 520,228 520,305 428,312" fill="var(--light)"/>
    <polygon points="428,330 520,325 520,420 405,395" fill="var(--navy)"/>
    <circle cx="255" cy="315" r="170" fill="#fff"/>
    <circle cx="255" cy="315" r="158" fill="none" stroke="var(--sky)" stroke-width="3"/>
    <defs>
      <linearGradient id="tower1" x1="0" y1="0" x2="0" y2="1">
        <stop offset="0" stop-color="#d6e3ee"/><stop offset=".6" stop-color="#8ea6ba"/><stop offset="1" stop-color="#5b7488"/>
      </linearGradient>
    </defs>
    <circle cx="255" cy="315" r="150" fill="url(#tower1)" role="img" aria-label="Photo of a modern glass office tower against a pale sky"/>
  </svg>
  <div class="brand-name" style="left:0;right:0;top:52px;justify-content:center"><span class="dot"></span>BRISVALE</div>
  <h1 class="cover-headline" style="top:520px"><span class="l1">YOUR CLEANING</span><span class="l2">IS OUR BUSINESS</span></h1>
  <div class="cover-rule" style="top:612px"></div>
  <div class="cover-url" style="top:626px">www.brisvale.ca</div>
</section>

<!-- ROW 2: inside spread -->
<section class="page inside-left" style="left:80px;top:792px">
  <h2 class="intro-title">YOUR CLEANING IS<br><span>OUR BUSINESS</span></h2>
  <p class="intro-copy">Brisvale, a Janitorial Services Company that has been in business since 1985, takes pride in providing the highest possible quality of janitorial and complete cleaning services for any type/size operation. Brisvale provides services to clients in the GTA, Southern Ontario, and many areas across Canada.</p>
  <h2 class="section-title">OUR SERVICES</h2>
  <div class="services-panel">
    <div class="service" style="top:10px"><span class="badge" role="img" aria-label="Cleanroom service icon"><i></i></span><h3>CLEANROOM &amp; GMP SERVICES</h3><p>Brisvale is a leading Cleanroom and GMP services cleaning company with an impressive performance record.</p></div>
    <div class="service" style="top:78px"><span class="badge" role="img" aria-label="Janitorial service icon"><i></i></span><h3>JANITORIAL SERVICES</h3><p>Brisvale provides complete janitorial services for any type/size operation. We currently service both public and private sectors.</p></div>
    <div class="service" style="top:146px"><span class="badge" role="img" aria-label="Carpet cleaning icon"><i></i></span><h3>CARPET &amp; UPHOLSTERY SERVICES</h3><p>Office furnishings such as carpets, drapes and upholstered furniture represent a serious investment to a company.</p></div>
    <div class="service" style="top:214px"><span class="badge" role="img" aria-label="Window cleaning icon"><i></i></span><h3>WINDOW CLEANING SERVICES</h3><p>We can implement a regular program of interior and exterior window cleaning, or we can meet your needs as project basis.</p></div>
    <div class="service" style="top:282px"><span class="badge" role="img" aria-label="Restoration service icon"><i></i></span><h3>FIRE AND FLOOD RESTORATION SERVICES</h3><p>Brisvale can provide full Fire and Flood Restoration services.</p></div>
    <div class="service" style="top:350px"><span class="badge" role="img" aria-label="Cleaning supplies icon"><i></i></span><h3>SANITATION SUPPLIES</h3><p>Brisvale supplies the highest quality janitorial supplies, contact us for a full list of supplies in stock.</p></div>
  </div>
</section>
<div class="spread-fold" style="left:600px;top:792px"></div>
<section class="page inside-right" style="left:600px;top:792px">
  <div class="qc-band"><h2>QUALITY CONTROL<br><span>SYSTEM</span></h2><p>Brisvale, a Janitorial Services Company that has been in business since 1985, takes pride in providing the highest possible quality of janitorial and complete cleaning services for any type/size operation. Brisvale provides services to clients in the GTA, Southern Ontario, and many areas across Canada.</p></div>
  <svg class="art" width="520" height="673" viewBox="0 0 520 673" style="pointer-events:none">
    <defs>
      <linearGradient id="hall" x1="0" y1="0" x2="1" y2="1"><stop offset="0" stop-color="#c9b7a3"/><stop offset=".5" stop-color="#6e5846"/><stop offset="1" stop-color="#3a3330"/></linearGradient>
      <linearGradient id="facade" x1="0" y1="0" x2="1" y2="1"><stop offset="0" stop-color="#bfe3f5"/><stop offset="1" stop-color="#2a95d6"/></linearGradient>
    </defs>
    <circle cx="140" cy="140" r="104" fill="#fff"/>
    <circle cx="140" cy="140" r="100" fill="url(#hall)" stroke="var(--sky)" stroke-width="3" role="img" aria-label="Photo of a cleaning cart in a clean office corridor"/>
    <circle cx="380" cy="790" r="190" fill="url(#facade)" stroke="var(--sky)" stroke-width="4" role="img" aria-label="Photo of window cleaners on a glass building facade"/>
  </svg>
  <div class="feature" style="left:34px;top:262px"><h4><svg width="18" height="18" viewBox="0 0 18 18"><circle cx="9" cy="9" r="8" fill="var(--sky)"/><path d="M5 9.5l2.6 2.5L13 6" stroke="#fff" stroke-width="1.8" fill="none"/></svg>Inspections</h4><p>Track trends to improve service. Perform detailed inspections. Track job performance. Correct deficiencies.</p></div>
  <div class="feature" style="left:270px;top:262px"><h4><svg width="18" height="18" viewBox="0 0 18 18"><circle cx="9" cy="9" r="8" fill="var(--sky)"/><circle cx="9" cy="9" r="4.5" fill="none" stroke="#fff" stroke-width="1.4"/><path d="M9 6.5V9l1.8 1.2" stroke="#fff" stroke-width="1.3" fill="none"/></svg>Job Scheduling</h4><p>Track compliance to contract specifications. Customize schedules to customer needs. Record daily and periodic services. Set automatic reminders.</p></div>
  <div class="feature" style="left:34px;top:356px"><h4><svg width="18" height="18" viewBox="0 0 18 18"><circle cx="9" cy="9" r="8" fill="var(--sky)"/><rect x="5.5" y="5" width="7" height="8" fill="none" stroke="#fff" stroke-width="1.3"/></svg>Work order management</h4><p>Instantly distribute work orders to those responsible. Automatically escalate work orders to management. Single point communications. Change/Cancel work orders.</p></div>
  <div class="feature" style="left:270px;top:356px"><h4><svg width="18" height="18" viewBox="0 0 18 18"><circle cx="9" cy="9" r="8" fill="var(--sky)"/><path d="M6 6h6M6 9h6M6 12h4" stroke="#fff" stroke-width="1.3"/></svg>Reports</h4><p>Identify which areas of a building require more attention. Address employee issues found during an inspection. Productivity tracking and control. Quality tracking and statistics.</p></div>
  <div class="timekeeping">
    <h3>AUTOMATED TIME KEEPING</h3>
    <p>Brisvale meets the increasing need for information accuracy and reliability with a computerised timekeeping system. Brisvale has realtime control of employees.</p>
    <ul>
      <li>Realtime employee communications to improve morale and engagement</li>
      <li>Realtime management of hours worked</li>
      <li>Realtime no show alerts</li>
      <li>Realtime on site attendance checks</li>
    </ul>
  </div>
</section>

<!-- ROW 3: outside spread -->
<section class="page back-cover" style="left:80px;top:1524px">
  <svg class="art" width="520" height="673" viewBox="0 0 520 673">
    <defs>
      <linearGradient id="washers" x1="0" y1="0" x2="1" y2="1"><stop offset="0" stop-color="#d8dde0"/><stop offset=".6" stop-color="#8f9aa0"/><stop offset="1" stop-color="#4d5a61"/></linearGradient>
    </defs>
    <rect x="0" y="150" width="520" height="270" fill="var(--navy)"/>
    <circle cx="110" cy="640" r="224" fill="#fff"/>
    <circle cx="110" cy="640" r="218" fill="none" stroke="var(--sky)" stroke-width="4"/>
    <circle cx="110" cy="640" r="212" fill="url(#washers)" role="img" aria-label="Photo of window cleaners working on a suspended platform"/>
  </svg>
  <div class="brand-name" style="left:0;right:0;top:66px;justify-content:center;font-size:30px"><span class="dot"></span>BRISVALE</div>
  <div class="contact-block">
    <h2>CONTACT INFO</h2>
    <div class="contact-line"><svg width="16" height="16" viewBox="0 0 16 16"><circle cx="8" cy="8" r="7" fill="none" stroke="#fff" stroke-width="1.2"/><path d="M5.5 4.5l1.5 1.5-1 1.2a5 5 0 0 0 2.8 2.8l1.2-1 1.5 1.5-1 1a6 6 0 0 1-6-6z" fill="#fff"/></svg>1 (866) 555-0142</div>
    <div class="contact-line"><svg width="18" height="13" viewBox="0 0 18 13"><rect x="1" y="1" width="16" height="11" fill="none" stroke="#fff" stroke-width="1.2"/><path d="M1 1l8 6 8-6" fill="none" stroke="#fff" stroke-width="1.2"/></svg>info@brisvale.ca</div>
    <div class="contact-line"><svg width="16" height="16" viewBox="0 0 16 16"><circle cx="8" cy="8" r="7" fill="none" stroke="#fff" stroke-width="1.2"/><ellipse cx="8" cy="8" rx="3" ry="7" fill="none" stroke="#fff" stroke-width="1"/><path d="M1 8h14" stroke="#fff" stroke-width="1"/></svg>www.brisvale.ca</div>
    <div class="contact-hours">Monday - Friday 9am-5pm</div>
  </div>
  <div class="social" aria-label="Social media links"><span></span><span></span></div>
</section>
<div class="spread-fold" style="left:600px;top:1524px"></div>
<section class="page front-cover" style="left:600px;top:1524px">
  <svg class="art" width="520" height="673" viewBox="0 0 520 673">
    <defs>
      <linearGradient id="tower2" x1="0" y1="0" x2="0" y2="1">
        <stop offset="0" stop-color="#d6e3ee"/><stop offset=".6" stop-color="#8ea6ba"/><stop offset="1" stop-color="#5b7488"/>
      </linearGradient>
    </defs>
    <rect x="0" y="150" width="180" height="270" fill="var(--navy)"/>
    <polygon points="345,120 520,95 520,205 405,238" fill="var(--navy)"/>
    <polygon points="420,255 520,228 520,305 428,312" fill="var(--light)"/>
    <polygon points="428,330 520,325 520,420 405,395" fill="var(--navy)"/>
    <circle cx="255" cy="315" r="170" fill="#fff"/>
    <circle cx="255" cy="315" r="158" fill="none" stroke="var(--sky)" stroke-width="3"/>
    <circle cx="255" cy="315" r="150" fill="url(#tower2)" role="img" aria-label="Photo of a modern glass office tower against a pale sky"/>
  </svg>
  <div class="brand-name" style="left:0;right:0;top:52px;justify-content:center"><span class="dot"></span>BRISVALE</div>
  <h1 class="cover-headline" style="top:520px"><span class="l1">YOUR CLEANING</span><span class="l2">IS OUR BUSINESS</span></h1>
  <div class="cover-rule" style="top:612px"></div>
  <div class="cover-url" style="top:626px">www.brisvale.ca</div>
</section>

</body>
</html>
```